Business Card Design Project

We need a business card design for our company kB7 s.r.o. The company is based in Slovakia and selling massage, yoga and meditation accessories online and offline. At the place where the offices are, we have a yoga studio, massage room, show room and shop as well. We will give the business card for customers who visit our shop or show room personally and for the new suppliers of demanded products we are visiting in the future.
I would like to have:
- small logo and datas on one side
- big logo and our main e-shops on the other side:
- www.pohodlnelavice.sk
- www.relaxnipultiky.cz
Datas:
Peter Kolar, MSc. / CEO
kB7 s.r.o.
Borovicová 742/3
938 05 Dunajská Streda
Slovak republic (Slovakia)
Office tel.: +421 (0) 917 604 382
Private tel.: +421 (0) 911 758 026
E-mail: info@kb7.sk
Web: www.kb7.sk
It is up to you if you use graphics emphasizing our profile or leave it simple and modern without pics. Looking forward to receiving your designs! Thank You!

```html
<!DOCTYPE html>
<html lang="sk">
<head>
<meta charset="utf-8">
<title>kB7 s.r.o. – business card</title>
<link rel="stylesheet" href="https://fonts.googleapis.com/css2?family=Arimo:wght@400;700&display=swap">
<style>
  :root {
    --page: #e9e9ea;
    --card: #ffffff;
    --slate: #4e5c68;
    --slate-dark: #3b4752;
    --orange: #f47b20;
    --ink: #1e1e1e;
    --muted: #8a9098;
  }
  * { box-sizing: border-box; margin: 0; padding: 0; }
  html, body {
    width: 1200px; height: 900px; overflow: hidden;
    background: var(--page);
    font-family: "Arimo", Arial, sans-serif;
  }
  .canvas {
    width: 1200px; height: 900px;
    display: flex; flex-direction: column; align-items: center;
    justify-content: center; gap: 40px;
  }
  .card {
    position: relative;
    width: 620px; height: 380px;
    background: var(--card);
    border-radius: 22px;
    overflow: hidden;
    box-shadow: 0 6px 18px rgba(0,0,0,0.14);
  }
  .wordmark {
    display: flex; align-items: center; gap: 10px;
    font-weight: 700; color: var(--slate);
    letter-spacing: -0.02em; line-height: 1;
  }
  .wordmark .dot {
    border-radius: 50%; background: var(--orange); flex: none;
  }

  /* Back side */
  .card-back .swoosh { position: absolute; inset: 0; }
  .card-back .wordmark {
    position: absolute; left: 60px; top: 60px;
    font-size: 120px;
  }
  .card-back .wordmark .dot { width: 30px; height: 30px; }
  .eshops {
    position: absolute; right: 34px; bottom: 30px;
    text-align: right; color: #fff;
    font-size: 17px; font-weight: 700; line-height: 1.45;
    letter-spacing: 0.01em;
  }

  /* Front side */
  .card-front .wordmark {
    position: absolute; left: 50px; top: 140px;
    font-size: 78px;
  }
  .card-front .wordmark .dot { width: 20px; height: 20px; }
  .divider {
    position: absolute; left: 300px; top: 90px;
    width: 2px; height: 210px;
    background: linear-gradient(to bottom, rgba(78,92,104,0), var(--slate) 45%, rgba(78,92,104,0));
  }
  .details {
    position: absolute; left: 332px; top: 92px;
    color: var(--ink);
  }
  .details .name { font-size: 24px; font-weight: 700; }
  .details .role { font-size: 15px; color: var(--orange); margin-top: 3px; }
  .details .address { font-size: 14px; line-height: 1.35; margin-top: 14px; }
  .contacts { list-style: none; margin-top: 8px; font-size: 14px; line-height: 1.4; }
  .contacts li { display: flex; align-items: center; gap: 8px; }
  .contacts svg { width: 14px; height: 14px; flex: none; fill: var(--ink); }
</style>
</head>
<body>
<main class="canvas">

  <section class="card card-back" aria-label="Back side">
    <svg class="swoosh" viewBox="0 0 620 380" preserveAspectRatio="none" aria-hidden="true">
      <path d="M505 0 Q455 250 255 380 L620 380 L620 0 Z" fill="var(--orange)"/>
      <path d="M468 0 Q418 245 222 380 L246 380 Q440 255 494 0 Z" fill="var(--slate)"/>
    </svg>
    <div class="wordmark"><span>kB7</span><span class="dot"></span></div>
    <div class="eshops">
      <p>www.relaxnipultiky.cz</p>
      <p>www.pohodlnelavice.sk</p>
    </div>
  </section>

  <section class="card card-front" aria-label="Front side">
    <div class="wordmark"><span>kB7</span><span class="dot"></span></div>
    <div class="divider"></div>
    <div class="details">
      <p class="name">Peter Kolar, MSc.</p>
      <p class="role">Chief Executive Officer</p>
      <p class="address">Borovicová 742/3<br>938 05 Dunajská Streda</p>
      <ul class="contacts">
        <li><svg viewBox="0 0 16 16"><path d="M2 5c0-2 2-3 6-3s6 1 6 3v1h-3V5H5v1H2zM3 7h10l1 6H2zm5 1.5a2 2 0 100 4 2 2 0 000-4z"/></svg>+421 (0) 917 604 382</li>
        <li><svg viewBox="0 0 16 16"><path d="M4 1h8v14H4zM5.5 2.5v9h5v-9zM7 12.5h2v1H7z"/></svg>+421 (0) 911 758 026</li>
        <li><svg viewBox="0 0 16 16"><path d="M1 3h14v10H1zm1.5 1.5v.3L8 9l5.5-4.2v-.3zm0 2.2v4.8h11V6.7L8 11z"/></svg>info@kb7.sk</li>
        <li><svg viewBox="0 0 16 16"><path d="M8 1a7 7 0 100 14A7 7 0 008 1zm0 1.5c.8 0 1.7 1.6 2 4H6c.3-2.4 1.2-4 2-4zM6 8h4c-.1 3-1 5.5-2 5.5S6.1 11 6 8zM2.6 8h2c0 2 .4 3.8 1 5A5.5 5.5 0 012.6 8zm8.8 0h2a5.5 5.5 0 01-3 5c.6-1.2 1-3 1-5z"/></svg>www.kb7.sk</li>
      </ul>
    </div>
  </section>

</main>
</body>
</html>
```